Refer a Friend A5 Flyer for Healthcare Staff

We need an A5 flyer that we can hand out to existing and new staff members promoting our Refer a friend Scheme. We need the leaflet to encourage staff to talk to their family and friends about joining our Healthcare Agency, which provides staff to local care related establishments. Using our logo and brand colours blue and green, as per our website, the final design will need to clearly convey the benefits and attractions of referring additional staff to the team. In addition is the promotion of our SocialHub page, requesting staff to like the page and to like and share various posts.

Target Market(s)

Healthcare and potential Healthcare Staff

Industry/Entity Type

Healthcare

Colors
33b8a4
3277b5

Requirements
Must have
• Company Logo, Brand colours,
• text; "Refer a Friend and receive a £50 Bonus after just 1 completed shift"
• text; "3 easy steps to refer a friend, 1 Fill out your name on the back of your Business Card 2 Hand the card to your friend or any person you wish to refer, 3 ask your friend to present the card to us when they attend their interview"
• text; "Like and share any of our Open Days on SocialHub for a chance to win a prize, you can find us easily by searching @CarewellPlacementGroup"
• text; "Like our Page to stay up to date with our events and offers"
Nice to have
• care worker / elderly care / support worker pictures
• Content / pics from website www.carewellplacementgroup.co.uk

```html
<!DOCTYPE html>
<html lang="en">
<head>
<meta charset="utf-8">
<title>Refer a Friend Flyer – Carewell Placement</title>
<link rel="stylesheet" href="https://fonts.googleapis.com/css2?family=Arimo:wght@700&family=Open+Sans:wght@400;700&display=swap">
<style>
  :root {
    --page-bg: #c9c4bb;
    --paper: #ffffff;
    --brand-blue: #0b4f9c;
    --brand-teal: #1bb59f;
    --ink-dark: #1c2740;
    --ink-body: #1a1a1a;
    --garden-dark: #4f7a3a;
    --garden-mid: #7fa257;
    --garden-light: #c8d6b0;
    --garden-warm: #d9744f;
    --team-light: #eef4fa;
    --team-mid: #c9dbec;
  }
  * { margin: 0; padding: 0; box-sizing: border-box; }
  html, body { width: 900px; height: 1200px; overflow: hidden; }
  body { background: var(--page-bg); font-family: "Open Sans", Arial, sans-serif; }

  .flyer {
    position: absolute; left: 79px; top: 75px;
    width: 744px; height: 1055px;
    background: var(--paper); overflow: hidden;
    box-shadow: 3px 4px 8px rgba(0,0,0,0.35);
  }
  .hero-art { position: absolute; left: 0; top: 0; }

  .team-photo {
    position: absolute; left: 440px; top: 172px;
    width: 304px; height: 362px;
  }

  .brand-name {
    position: absolute; right: 22px; top: 30px;
    font-family: "Open Sans", Arial, sans-serif; font-weight: 400;
    font-size: 34px; line-height: 1.08; color: var(--brand-blue);
    text-align: right;
  }

  .headline {
    position: absolute; left: 24px; top: 480px;
    font-family: "Arimo", Arial, sans-serif; font-weight: 700;
    font-size: 70px; line-height: 0.98; color: var(--brand-blue);
    letter-spacing: 1.5px;
  }
  .intro {
    position: absolute; left: 23px; top: 622px; width: 680px;
    font-size: 26px; line-height: 38px; color: var(--ink-body);
  }

  .referral-band {
    position: absolute; left: 0; top: 710px; width: 744px; height: 136px;
    background: var(--brand-teal); padding: 20px 24px 0 24px;
  }
  .referral-band li {
    list-style: none; position: relative; padding-left: 20px;
    font-weight: 700; font-size: 14.8px; line-height: 21.5px; color: var(--ink-dark);
    margin-bottom: 13px;
  }
  .referral-band svg { position: absolute; left: 0; top: 4px; }

  .social-copy {
    position: absolute; left: 22px; top: 856px; width: 690px;
    font-weight: 700; font-size: 19px; line-height: 28px; color: var(--brand-blue);
  }
  .social-copy p + p { margin-top: 12px; }

  .web-band {
    position: absolute; left: 0; top: 975px; width: 744px; height: 80px;
    background: var(--brand-blue);
    display: flex; align-items: center; justify-content: center;
    font-family: "Arimo", Arial, sans-serif; font-weight: 700;
    font-size: 37px; color: #ffffff;
  }
</style>
</head>
<body>
  <main class="flyer">
    <svg class="hero-art" width="744" height="480" viewBox="0 0 744 480">
      <defs>
        <clipPath id="careClip"><path d="M0,0 L466,0 C440,230 300,430 0,462 Z"/></clipPath>
        <linearGradient id="gardenBase" x1="0" y1="0" x2="0.8" y2="1">
          <stop offset="0" stop-color="var(--garden-light)"/>
          <stop offset="0.35" stop-color="var(--garden-mid)"/>
          <stop offset="1" stop-color="var(--garden-dark)"/>
        </linearGradient>
        <radialGradient id="warmGlow" cx="0.5" cy="0.5" r="0.5">
          <stop offset="0" stop-color="var(--garden-warm)" stop-opacity="0.85"/>
          <stop offset="0.6" stop-color="var(--garden-warm)" stop-opacity="0.35"/>
          <stop offset="1" stop-color="var(--garden-warm)" stop-opacity="0"/>
        </radialGradient>
        <radialGradient id="softLight" cx="0.5" cy="0.5" r="0.5">
          <stop offset="0" stop-color="#dfeadf" stop-opacity="0.8"/>
          <stop offset="1" stop-color="#dfeadf" stop-opacity="0"/>
        </radialGradient>
        <linearGradient id="teamGlow" x1="0" y1="0" x2="0" y2="1">
          <stop offset="0" stop-color="var(--team-light)"/>
          <stop offset="0.5" stop-color="var(--team-mid)"/>
          <stop offset="1" stop-color="var(--team-light)"/>
        </linearGradient>
      </defs>
      <g role="img" aria-label="Photo of a smiling carer standing behind an elderly woman in a wheelchair in a garden" clip-path="url(#careClip)">
        <rect width="470" height="470" fill="url(#gardenBase)"/>
        <ellipse cx="250" cy="60" rx="210" ry="90" fill="url(#softLight)"/>
        <ellipse cx="210" cy="300" rx="150" ry="130" fill="url(#warmGlow)"/>
      </g>
      <path d="M466,0 C440,230 300,430 0,462" fill="none" stroke="var(--brand-blue)" stroke-width="9"/>
    </svg>

    <svg class="team-photo" viewBox="0 0 304 362" role="img" aria-label="Photo of a group of healthcare staff in light uniforms joining hands in a circle">
      <defs>
        <linearGradient id="teamFill" x1="0" y1="0" x2="1" y2="1">
          <stop offset="0" stop-color="var(--team-light)"/>
          <stop offset="0.55" stop-color="var(--team-mid)"/>
          <stop offset="1" stop-color="var(--team-light)"/>
        </linearGradient>
      </defs>
      <rect x="0" y="0" width="304" height="362" rx="6" fill="url(#teamFill)"/>
    </svg>

    <div class="brand-name">Carewell<br>Placement</div>

    <h1 class="headline">SUPERIOR<br>SOLUTIONS</h1>
    <p class="intro">We supply qualified, experienced local staff, dedicated to delivering excellent services.</p>

    <ul class="referral-band">
      <li>
        <svg width="13" height="13" viewBox="0 0 13 13"><circle cx="6.5" cy="6.5" r="5.5" fill="none" stroke="var(--ink-dark)" stroke-width="1.2"/><path d="M3.8,6.6 L5.8,8.5 L9.4,4.6" fill="none" stroke="var(--ink-dark)" stroke-width="1.4"/></svg>
        Refer a Friend &amp; receive a £50 Bonus after just 1 completed shift.
      </li>
      <li>
        <svg width="13" height="13" viewBox="0 0 13 13"><circle cx="6.5" cy="6.5" r="5.5" fill="none" stroke="var(--ink-dark)" stroke-width="1.2"/><path d="M3.8,6.6 L5.8,8.5 L9.4,4.6" fill="none" stroke="var(--ink-dark)" stroke-width="1.4"/></svg>
        3 easy steps to refer a friend, 1 Fill out your name on the back of your Business Card 2 Hand the card to your friend or any person you wish to refer, 3 ask your friend to present the card to us when they attend their interview.
      </li>
    </ul>

    <div class="social-copy">
      <p>Like and share any of our Open Days on SocialHub for a chance to win a prize, you can find us easily by searching @CarewellPlacementGroup</p>
      <p>Like our Page to stay up to date with our events &amp; offers</p>
    </div>

    <footer class="web-band">www.carewellplacementgroup.co.uk</footer>
  </main>
</body>
</html>
```